Foot and ankle surgeon requires a website design

I need a website where prospective and established patients can obtain information and then direct them to making appointments. My practice is a highly professional surgical practice specialising in surgery to the foot and ankle. My title is Mr Colin Dwyer, Podiatric Foot & Ankle Surgeon. My qualifications are: BSc MSc FACPS
The practice website will require information on: Locations, phone numbers to make appointments, general background on podiatric surgery,
I would like to include information on: my hospital appointments, surgical fellowships held, training programs undertaken, association memberships, publications written, links to useful websites
A page dedicated to common foot conditions would be useful and also a page with referral information including an online registration section that will be sent direct to the receptionist.
Examples of similar websites include:
http://www.trevorkeplinfeet.com.au/
http://www.vollardfootsurgeon.com.au/
I will provide files on logo, self photos and my personal training history etc.
Also if there is going to be a background theme I personally am associated with surfing and beach activities, it would be great if this was able to be reflected in the design.
Thank you.

```html
<!DOCTYPE html>
<html lang="en">
<head>
<meta charset="utf-8">
<title>Mr Colin Dwyer – Podiatric Foot &amp; Ankle Surgeon</title>
<link rel="stylesheet" href="https://fonts.googleapis.com/css2?family=Arimo:wght@400;700&family=Open+Sans:wght@400;600;700&family=Roboto+Condensed:wght@400&family=Tinos:wght@400;700&display=swap">
<style>
:root{
  --navy:#1e4f87;
  --navy-dark:#1b4577;
  --panel:#235184;
  --orange:#ef6f1f;
  --orange-light:#f5923a;
  --heading:#1f4f86;
  --link-blue:#2a5d94;
  --text:#6b6b6b;
  --text-dark:#444;
  --rule:#bfbfbf;
  --section-bg:#f4f4f4;
  --footer:#3d3d3d;
  --white:#fff;
}
*{box-sizing:border-box;margin:0;padding:0}
html,body{width:1002px;height:1200px;overflow:hidden;background:var(--white)}
body{position:relative;font-family:"Open Sans",sans-serif;color:var(--text)}
.abs{position:absolute}

/* hero */
.hero-photo{left:0;top:0;width:1002px;height:499px;
  background:radial-gradient(ellipse at 30% 55%,#e0a27c 0%,#c98a63 30%,rgba(220,190,140,.6) 60%,transparent 80%),
  linear-gradient(90deg,#c79b78 0%,#e8d6ac 45%,#f0e2b6 70%,#e9d9ad 100%)}
.nav-bar{left:0;top:5px;width:1002px;height:43px;background:var(--navy)}
.nav{left:337px;top:5px;width:665px;height:43px;background:var(--navy);border-top-left-radius:18px;
  display:flex;align-items:center;padding-left:25px;font-family:"Roboto Condensed",sans-serif;font-size:14px;color:var(--white)}
.nav span.sep{margin:0 14px}
.logo-box{left:83px;top:0;width:253px;height:129px;background:var(--white);border-radius:0 0 12px 12px;
  display:flex;align-items:center;gap:10px;padding-left:20px}
.logo-mark{width:22px;height:22px;border-radius:50%;background:var(--orange);flex:none}
.logo-name{font-family:"Tinos",serif;font-weight:700;font-size:20px;color:var(--navy-dark);line-height:1.15}

/* booking panel */
.booking{left:644px;top:150px;width:274px;height:311px;background:var(--panel);border-radius:7px;padding:16px 22px}
.booking h2{font-family:"Tinos",serif;font-size:23px;color:var(--white);font-weight:700;margin-bottom:14px;white-space:nowrap}
.field{width:218px;height:29px;background:var(--white);margin-bottom:9px;font-family:"Arimo",sans-serif;font-size:12px;color:#888;padding:7px 8px}
.label{font-family:"Arimo",sans-serif;font-weight:700;font-size:11.5px;color:var(--white);margin:6px 0 6px 2px}
.selects{display:flex;gap:8px;margin-bottom:8px}
.select{height:25px;background:var(--white);border-radius:5px;font-family:"Arimo",sans-serif;font-size:12px;color:#888;padding:5px 10px;position:relative}
.select::after{content:"";position:absolute;right:7px;top:8px;border:3px solid transparent;border-bottom:3px solid #333;border-top:none}
.select::before{content:"";position:absolute;right:7px;top:13px;border:3px solid transparent;border-top:3px solid #333;border-bottom:none}
.book-btn{width:218px;height:32px;margin-top:12px;border-radius:6px;background:linear-gradient(var(--orange-light),var(--orange));
  color:var(--white);font-family:"Open Sans",sans-serif;font-weight:700;font-size:17px;letter-spacing:1.3px;text-align:center;line-height:32px}

/* intro */
.intro{left:0;top:499px;width:1002px;height:374px;background:var(--section-bg);border-bottom:2px solid #e2e2e2}
.intro-title{left:0;top:524px;width:1002px;text-align:center;font-family:"Tinos",serif;font-size:28px;color:var(--heading)}
.intro-rule{left:83px;top:568px;width:835px;height:1px;background:var(--rule)}
.lead{left:81px;top:588px;width:292px}
.lead h3{font-weight:400;font-size:14px;color:var(--text-dark);margin-bottom:3px}
.lead p{font-size:11px;line-height:18.5px;margin-bottom:4px}
.read-more{display:inline-block;margin-top:10px;width:104px;height:30px;background:linear-gradient(#4d73a3,var(--navy-dark));border-radius:3px;
  color:var(--white);font-family:"Roboto Condensed",sans-serif;font-size:12px;text-align:center;line-height:30px}
.feature{width:258px}
.feature .frame{width:258px;height:112px;background:var(--white);border:1px solid #ddd;padding:5px}
.feature .photo{width:100%;height:100%}
.feature h3{font-size:18px;font-weight:600;color:var(--link-blue);margin:12px 0 6px}
.feature p{font-size:11px;line-height:18.5px;padding-left:2px}

/* conditions */
.cond-title{left:103px;top:895px;font-family:"Tinos",serif;font-size:24px;color:var(--heading)}
.cond-rule{left:380px;top:914px;width:494px;height:1px;background:var(--rule)}
.arrow{top:978px}
.card{top:951px;width:160px;text-align:center}
.card .photo{width:160px;height:89px;border-radius:8px}
.card span{display:block;margin-top:10px;font-family:"Arimo",sans-serif;font-size:14px;color:var(--link-blue)}
.skin{background:linear-gradient(160deg,#c99b85,#a8725d 60%,#8f5e4a)}
.cast{background:linear-gradient(90deg,#a5a5a5 0%,#c9b0a2 40%,#c6a28f 70%,#e6e6e6 100%)}

/* footer */
.footer{left:0;top:1117px;width:1002px;height:83px;background:var(--footer)}
.foot-links{left:93px;top:1139px;font-family:"Arimo",sans-serif;font-size:12px;color:var(--white)}
.foot-links .sep{margin:0 13px}
.copyright{left:93px;top:1164px;font-family:"Arimo",sans-serif;font-size:12px;color:var(--white)}
.social{top:1137px;width:42px;height:42px;border-radius:50%}
</style>
</head>
<body>

<div class="abs hero-photo" role="img" aria-label="Photograph of hands massaging a patient's foot"></div>
<div class="abs nav-bar"></div>
<nav class="abs nav">
  <span>HOME</span><span class="sep">|</span><span>ABOUT</span><span class="sep">|</span><span>PATIENTS</span><span class="sep">|</span><span>PODIATRIC SURGERY</span><span class="sep">|</span><span>APPOINTMENTS</span><span class="sep">|</span><span>BLOG</span><span class="sep">|</span><span>FAQ</span>
</nav>
<div class="abs logo-box">
  <div class="logo-mark"></div>
  <div class="logo-name">Mr Colin Dwyer</div>
</div>

<form class="abs booking">
  <h2>Hopital Appointments</h2>
  <div class="field">Name</div>
  <div class="field">Contact Number</div>
  <div class="label">Preferred Date?</div>
  <div class="selects">
    <div class="select" style="width:55px">Day</div>
    <div class="select" style="width:92px">Month</div>
  </div>
  <div class="label">Preferred Time?</div>
  <div class="selects">
    <div class="select" style="width:55px">12</div>
    <div class="select" style="width:55px">00</div>
    <div class="select" style="width:55px">am</div>
  </div>
  <div class="book-btn">Request Booking</div>
</form>

<section class="abs intro"></section>
<h1 class="abs intro-title">Mr.Colin Dwyer Podiatric Foot &amp; Ankle Surgeon</h1>
<div class="abs intro-rule"></div>

<div class="abs lead">
  <h3>Nulla sit amet diam Duis non nunc</h3>
  <p>libero a tempus libero lectus feugiat felis Morbi diam mauris viverra in gravida eu mattis in ante Morbi eget arcu Morbi porta libero id ullamcorper nonummy nibh ligula pulvinar metus eget consv</p>
  <p>Morbi ornare gravida elit Integer congue augue et malesuada iaculis ipsum dui aliquet felis at cursus magna nisl nec elit Vestibulum gravida Praesent elementum elit at tellus Male-suada nec ultricies sit amet</p>
  <span class="read-more">READ MORE</span>
</div>

<div class="abs feature" style="left:389px;top:590px">
  <div class="frame"><div class="photo" style="background:linear-gradient(90deg,#8a8f86,#6f8fa6 45%,#c4a99c 70%,#ebebeb)" role="img" aria-label="Photograph of a foot during surgical treatment"></div></div>
  <h3>Why Choose Us</h3>
  <p>Aliquam nec erat at purus cursus interdum Vestibu-lum ligula augue bibendum accumsan vestibulum ut commodo a mi Morbi ornare gravida elit Integer congue augue et malesuada</p>
</div>
<div class="abs feature" style="left:661px;top:590px">
  <div class="frame"><div class="photo cast" role="img" aria-label="Photograph of a foot in an ankle brace"></div></div>
  <h3 style="margin-top:14px">Facilities &amp; Training</h3>
  <p>Aliquam nec erat at purus cursus interdum Vestibu-lum ligula augue bibendum accumsan vestibulum ut commodo a mi Morbi ornare gravida elit Integer congue augue et malesuada iaculis ipsum</p>
</div>

<h2 class="abs cond-title">Common Foot Conditions</h2>
<div class="abs cond-rule"></div>
<svg class="abs arrow" style="left:98px" width="18" height="30" viewBox="0 0 18 30"><polyline points="14,2 3,15 14,28" fill="none" stroke="#999" stroke-width="2"/></svg>
<svg class="abs arrow" style="left:886px" width="18" height="30" viewBox="0 0 18 30"><polyline points="4,2 15,15 4,28" fill="none" stroke="#999" stroke-width="2"/></svg>

<div class="abs card" style="left:132px"><div class="photo cast" role="img" aria-label="Photograph of a foot in an ankle brace"></div><span>Ankle Replacement</span></div>
<div class="abs card" style="left:325px"><div class="photo skin" role="img" aria-label="Photograph of a pair of bare feet"></div><span style="margin-top:12px">Ankle Trauma</span></div>
<div class="abs card" style="left:518px"><div class="photo cast" role="img" aria-label="Photograph of a foot in an ankle brace"></div><span style="margin-top:12px">Tendom Rupture</span></div>
<div class="abs card" style="left:708px"><div class="photo skin" role="img" aria-label="Photograph of a pair of bare feet"></div><span style="margin-top:12px">Ankle Pain</span></div>

<footer class="abs footer"></footer>
<div class="abs foot-links">
  <span>Home</span><span class="sep">|</span><span>About</span><span class="sep">|</span><span>Patients</span><span class="sep">|</span><span>Podiatric Surgery</span><span class="sep">|</span><span>Appointments</span><span class="sep">|</span><span>Blog</span><span class="sep">|</span><span>FAQ</span>
</div>
<div class="abs copyright">Copyright © 2014 Mr Colin Dwyer. All rights reserved.</div>
<div class="abs social" style="left:710px;background:#174a7e"></div>
<div class="abs social" style="left:764px;background:#1da1e6"></div>
<div class="abs social" style="left:818px;background:#f39419"></div>
<div class="abs social" style="left:872px;background:#bdbdbd"></div>

</body>
</html>
```